Redesigning of the packaging for 4 GOLDEN HEARTH gourmet breads

We need new designs for our range of four gourmet sliced breads, called GOLDEN HEARTH. These breads are prepared with specially selected ingredients sourced from several countries and with extreme focus on quality, health and indulgent pleasure. The Golden Hearth brand aims to solve the boring and bland nature of white breads and comes in several flavours such as coconut, seeds & nuts, exotic fruits and vegetables, buttermilk, chocolate, etc.
The Golden Hearth brand positioning statement is JOY IN EVERY SLICE
The current packaging designs are still quite attractive which makes it a difficult decision, but we know it's time for a rebrand, and therefore we really want the best possible designs - ONLY THE BEST!
GOLDEN HEARTH currently comprises three 'sister' products and one new addition named as follows:
1. Golden Hearth - buttermilk dream (yellow color)
2. Golden Hearth - cocoa swirl (brown & orange color)
3. Golden Hearth - tropic coconut (green & cream color)
4. Hearth Tots - (kiddies' style - This is a kiddies bread)
[Some pictures of the current packaging are attached, alongside with the content, layout and dimensions which should be used for the new designs, including ingredients, addresses, etc. Check the file 'Back view with ingredients and contents.pdf'; 'Layout and Dimensions of current Golden Hearth Packaging.pdf]
5. The logo may or may not be modified. (Golden Hearth Logo.pdf)
Key points to note:
- Demographic: The target audience is mainly young and middle aged from the middle to upper economic class
- Psychographic: Health conscious, Class conscious, Family focused consumers, Environment and Sustainable development minded consumers
- The designs will be similar in style for the 3 variants but be differentiated by colours and content
- The fonts and the overall design should be modern, playful and inviting.
- The content of the packaging is in the attachments
- Total designs - 4 designs.
Target Market(s)
The target market is kids, teens, young adults. Middle to upper economic class. Premium segment, lifestyle conscious consumers.
Industry/Entity Type
Bakery
Colors
Designer to choose colors to be used in the design.
Look and feel

```html
<!DOCTYPE html>
<html lang="en">
<head>
<meta charset="utf-8">
<title>Hearth Tots – Buttermilk Bread Pack</title>
<link href="https://fonts.googleapis.com/css2?family=Baloo+2:wght@800&family=Roboto+Condensed:wght@700&display=swap" rel="stylesheet">
<style>
  :root {
    --page: #ffffff;
    --blue-deep: #1552a3;
    --blue-mid: #2d7dd2;
    --blue-light: #8cc3f2;
    --glow: #ffffff;
    --brand-orange: #f07a10;
    --pill-orange: #f5a11c;
    --pill-shadow: #b86a0a;
    --pill-text: #ffffff;
    --heart-red: #e0261b;
    --heart-orange: #f27a22;
    --crust-light: #d9b68e;
    --crust-dark: #8f6a4d;
    --badge: #eaf2fb;
  }
  html, body {
    margin: 0;
    width: 1200px;
    height: 886px;
    overflow: hidden;
    background: var(--page);
  }
  .pack-sheet {
    display: block;
    width: 1200px;
    height: 886px;
  }
  .brand-name {
    font-family: "Baloo 2", "Arial Rounded MT Bold", sans-serif;
    font-weight: 800;
    fill: var(--brand-orange);
  }
  .flavour-label {
    font-family: "Roboto Condensed", "Arial Narrow", sans-serif;
    font-weight: 700;
    font-size: 21px;
    fill: var(--pill-text);
    letter-spacing: 0.4px;
  }
  .ray { fill: var(--glow); opacity: 0.16; }
  .sparkle { fill: url(#sparkle-glow); }
</style>
</head>
<body>
<svg class="pack-sheet" viewBox="0 0 1200 886" xmlns="http://www.w3.org/2000/svg">
  <defs>
    <linearGradient id="sky" x1="0" y1="0" x2="0" y2="1">
      <stop offset="0" stop-color="var(--blue-mid)"/>
      <stop offset="1" stop-color="var(--blue-deep)"/>
    </linearGradient>
    <radialGradient id="title-burst" cx="0.5" cy="0.5" r="0.5">
      <stop offset="0" stop-color="var(--glow)" stop-opacity="0.95"/>
      <stop offset="0.3" stop-color="var(--blue-light)" stop-opacity="0.6"/>
      <stop offset="1" stop-color="var(--blue-mid)" stop-opacity="0"/>
    </radialGradient>
    <radialGradient id="window-glow" cx="0.5" cy="0.5" r="0.5">
      <stop offset="0" stop-color="var(--glow)" stop-opacity="1"/>
      <stop offset="0.35" stop-color="var(--blue-light)" stop-opacity="0.55"/>
      <stop offset="1" stop-color="var(--blue-mid)" stop-opacity="0"/>
    </radialGradient>
    <radialGradient id="sparkle-glow" cx="0.5" cy="0.5" r="0.5">
      <stop offset="0" stop-color="var(--glow)" stop-opacity="0.95"/>
      <stop offset="0.45" stop-color="var(--glow)" stop-opacity="0.45"/>
      <stop offset="1" stop-color="var(--glow)" stop-opacity="0"/>
    </radialGradient>
    <linearGradient id="bread" x1="0" y1="0" x2="1" y2="1">
      <stop offset="0" stop-color="var(--crust-light)"/>
      <stop offset="1" stop-color="var(--crust-dark)"/>
    </linearGradient>

    <polygon id="ray" class="ray" points="0,0 460,-16 460,16"/>

    <!-- label artwork, origin at label top-left -->
    <g id="label-art">
      <rect class="label-field" x="0" y="0" width="1002" height="330" fill="url(#sky)"/>

      <g class="sunburst" transform="translate(190 140)">
        <use href="#ray" transform="rotate(0)"/>
        <use href="#ray" transform="rotate(20)"/>
        <use href="#ray" transform="rotate(40)"/>
        <use href="#ray" transform="rotate(60)"/>
        <use href="#ray" transform="rotate(80)"/>
        <use href="#ray" transform="rotate(100)"/>
        <use href="#ray" transform="rotate(120)"/>
        <use href="#ray" transform="rotate(140)"/>
        <use href="#ray" transform="rotate(160)"/>
        <use href="#ray" transform="rotate(180)"/>
        <use href="#ray" transform="rotate(200)"/>
        <use href="#ray" transform="rotate(220)"/>
        <use href="#ray" transform="rotate(240)"/>
        <use href="#ray" transform="rotate(260)"/>
        <use href="#ray" transform="rotate(280)"/>
        <use href="#ray" transform="rotate(300)"/>
        <use href="#ray" transform="rotate(320)"/>
        <use href="#ray" transform="rotate(340)"/>
      </g>
      <ellipse class="title-glow" cx="190" cy="140" rx="230" ry="170" fill="url(#title-burst)"/>
      <ellipse class="window-glow" cx="770" cy="150" rx="190" ry="160" fill="url(#window-glow)"/>

      <g class="sparkles">
        <circle class="sparkle" cx="110" cy="22" r="14"/>
        <circle class="sparkle" cx="330" cy="30" r="10"/>
        <circle class="sparkle" cx="40" cy="250" r="16"/>
        <circle class="sparkle" cx="120" cy="300" r="12"/>
        <circle class="sparkle" cx="250" cy="300" r="18"/>
        <circle class="sparkle" cx="360" cy="250" r="12"/>
        <circle class="sparkle" cx="290" cy="190" r="10"/>
        <circle class="sparkle" cx="680" cy="40" r="14"/>
        <circle class="sparkle" cx="700" cy="10" r="10"/>
        <circle class="sparkle" cx="820" cy="55" r="16"/>
        <circle class="sparkle" cx="890" cy="80" r="18"/>
        <circle class="sparkle" cx="940" cy="35" r="12"/>
        <circle class="sparkle" cx="880" cy="200" r="12"/>
        <circle class="sparkle" cx="860" cy="245" r="14"/>
        <circle class="sparkle" cx="930" cy="250" r="10"/>
        <circle class="sparkle" cx="780" cy="295" r="16"/>
        <circle class="sparkle" cx="960" cy="300" r="12"/>
      </g>

      <g class="bread-window">
        <path d="M409 330 C400 260 430 180 500 172 C545 168 575 178 592 196 C610 120 640 86 690 87 C745 90 770 170 754 250 L735 330 Z"
              fill="none" stroke="var(--heart-orange)" stroke-width="14"/>
        <path role="img" aria-label="Photo of sliced buttermilk bread loaf"
              d="M409 330 C400 260 430 180 500 172 C545 168 575 178 592 196 C610 120 640 86 690 87 C745 90 770 170 754 250 L735 330 Z"
              fill="url(#bread)" stroke="var(--heart-red)" stroke-width="6"/>
      </g>

      <g class="quality-badge">
        <ellipse cx="392" cy="82" rx="48" ry="32" fill="var(--badge)" opacity="0.9"/>
      </g>

      <text class="brand-name" x="40" y="160" font-size="80">HEARTH</text>
      <text class="brand-name" x="200" y="222" font-size="80">Tots</text>

      <g class="flavour-pill">
        <rect x="174" y="228" width="164" height="36" rx="18" fill="var(--pill-shadow)" transform="translate(2 3)"/>
        <rect x="174" y="228" width="164" height="36" rx="18" fill="var(--pill-orange)"/>
        <text class="flavour-label" x="256" y="254" text-anchor="middle">BUTTER MILK</text>
      </g>
    </g>

    <clipPath id="bag-body">
      <path d="M105 105 Q480 86 846 100 C872 112 878 200 876 252 L1040 112 L1062 108 L1052 196 L1072 258 L1056 330 L1062 394 L1040 390 L876 276 C878 330 868 384 840 386 Q480 394 104 385 Q90 245 105 105 Z"/>
    </clipPath>
    <clipPath id="flat-label">
      <rect x="78" y="477" width="1002" height="330"/>
    </clipPath>
  </defs>

  <!-- bagged loaf view -->
  <g class="bag-view" clip-path="url(#bag-body)">
    <rect x="90" y="80" width="1000" height="330" fill="url(#sky)"/>
    <ellipse cx="880" cy="258" rx="150" ry="130" fill="url(#window-glow)"/>
    <circle class="sparkle" cx="1010" cy="150" r="16"/>
    <circle class="sparkle" cx="1040" cy="330" r="14"/>
    <circle class="sparkle" cx="990" cy="360" r="10"/>
    <use href="#label-art" x="99" y="92"/>
  </g>

  <!-- flat label view -->
  <g class="flat-view" clip-path="url(#flat-label)">
    <use href="#label-art" x="78" y="477"/>
  </g>
</svg>
</body>
</html>
```